Dietitian needs a new business card design

I need a new business card design for my nutrition business that provides individual clinical nutrition advice for people with medical conditions. Business cards will be handed out to doctors, specialists and clients so will need to be sharp and project an image of professionalism

Target Market(s)

My clients are typically referred by doctors or specialists and the card will be used to handout to clients and their doctors.

Industry/Entity Type

Medical

Contact Information for Business Card

The business card will require the details below. These details can be found from my website https://www.kelvarrowclinic.com.au/

Font styles to use
Serif

Colors

Designer to choose colors to be used in the design.

Requirements
Must have
• 1. It needs be professional and contemporary
• 2. It needs to incorporate my logo
• 3. It needs space to write appointment times and dates
• 4. It needs to provide my phone number, fax number, email address and my web address
Nice to have
• Include the Registered Tovance Clinician Logo
• I have access to Framellow if required
• The locations I practise from
Should not have
• Pictures of food
• Spelling MIstakes

```html
<!DOCTYPE html>
<html lang="en">
<head>
<meta charset="utf-8">
<title>Kelvarrow Nutrition &amp; Dietetics – Business Card</title>
<link rel="stylesheet" href="https://fonts.googleapis.com/css2?family=Noto+Serif:wght@400;700&display=swap">
<style>
  :root {
    --bg: #2c2e31;
    --card: #ffffff;
    --blue: #1a5fb4;
    --blue-dark: #1b4f9c;
    --green: #7cbf2e;
    --line: #7a9cc8;
    --serif: "Noto Serif", Georgia, serif;
  }
  * { box-sizing: border-box; margin: 0; padding: 0; }
  html, body { width: 1200px; height: 900px; overflow: hidden; }
  body { background: var(--bg); font-family: var(--serif); position: relative; }

  .card {
    position: absolute;
    width: 520px; height: 300px;
    background: var(--card);
    border-radius: 22px;
    overflow: hidden;
  }

  /* Front */
  .card-front { left: 60px; top: 470px; }
  .brand {
    position: absolute; left: 250px; top: 34px;
    display: flex; align-items: center; gap: 10px;
  }
  .brand-dot { width: 30px; height: 30px; border-radius: 50%; background: var(--blue); flex: none; }
  .brand-name { color: var(--blue); font-size: 21px; font-weight: 700; line-height: 1.1; }
  .identity { position: absolute; left: 30px; top: 108px; width: 200px; text-align: right; }
  .identity .name { font-size: 32px; color: var(--blue); line-height: 1.1; }
  .identity .name span { color: var(--green); }
  .identity .title { font-size: 17px; color: var(--blue); margin-top: 4px; }
  .divider { position: absolute; left: 250px; top: 110px; width: 1px; height: 100px; background: var(--line); }
  .contacts { position: absolute; left: 268px; top: 122px; list-style: none; }
  .contacts li { display: flex; align-items: center; gap: 8px; font-size: 16px; color: var(--blue-dark); height: 26px; }
  .contacts svg { width: 18px; height: 18px; flex: none; }
  .address-band {
    position: absolute; left: 0; bottom: 0; width: 100%; height: 56px;
    background: var(--blue); color: #fff; font-size: 16px;
    display: flex; align-items: center; justify-content: center;
  }

  /* Back */
  .card-back { left: 620px; top: 130px; color: var(--blue); }
  .appt-heading { position: absolute; left: 34px; top: 26px; font-size: 30px; letter-spacing: 2px; font-weight: 400; }
  .field { position: absolute; display: flex; align-items: flex-end; font-size: 14px; }
  .field .rule { border-bottom: 1px dashed var(--line); height: 14px; margin-left: 4px; flex: 1; }
  .field-for { left: 34px; top: 88px; width: 370px; }
  .field-for2 { left: 34px; top: 118px; width: 370px; }
  .days { position: absolute; left: 34px; top: 150px; display: flex; gap: 12px; font-size: 14px; }
  .days span { display: flex; align-items: center; gap: 4px; }
  .days i { width: 13px; height: 13px; border: 1.5px solid var(--blue); border-radius: 50%; display: inline-block; }
  .field-date { left: 34px; top: 196px; width: 300px; }
  .field-time { left: 34px; top: 236px; width: 440px; }
  .field-time .ampm { margin-left: 6px; }
  .back-mark { position: absolute; right: 34px; top: 60px; width: 70px; height: 70px; border-radius: 50%; background: var(--blue); }
</style>
</head>
<body>

<section class="card card-back" aria-label="Appointment card">
  <h2 class="appt-heading">APPOINTMENT</h2>
  <div class="field field-for">FOR<span class="rule"></span></div>
  <div class="field field-for2"><span class="rule" style="margin-left:0"></span></div>
  <div class="days">
    <span><i></i>MON</span><span><i></i>TUE</span><span><i></i>WED</span>
    <span><i></i>THU</span><span><i></i>FRI</span><span><i></i>SAT</span>
  </div>
  <div class="field field-date">DATE<span class="rule"></span></div>
  <div class="field field-time">TIME<span class="rule"></span><span class="ampm">AM/PM</span></div>
  <div class="back-mark" aria-hidden="true"></div>
</section>

<section class="card card-front" aria-label="Business card front">
  <div class="brand">
    <span class="brand-dot" aria-hidden="true"></span>
    <span class="brand-name">Kelvarrow<br>Nutrition &amp; Dietetics</span>
  </div>
  <div class="identity">
    <div class="name">Your <span>Name</span></div>
    <div class="title">Your Title</div>
  </div>
  <div class="divider"></div>
  <ul class="contacts">
    <li>
      <svg viewBox="0 0 20 20"><circle cx="10" cy="10" r="10" fill="#7cbf2e"/><path d="M7 5.5l2 2-1.2 1.4c.7 1.5 1.8 2.6 3.3 3.3l1.4-1.2 2 2-1.5 1.5c-3.5-.5-6.5-3.5-7-7z" fill="#fff"/></svg>
      0123456789
    </li>
    <li>
      <svg viewBox="0 0 20 20"><circle cx="10" cy="10" r="10" fill="#7cbf2e"/><rect x="5" y="6.5" width="10" height="7" fill="none" stroke="#fff" stroke-width="1.3"/><path d="M5 6.5l5 4 5-4" fill="none" stroke="#fff" stroke-width="1.3"/></svg>
      youremail@mailpost.com
    </li>
    <li>
      <svg viewBox="0 0 20 20"><circle cx="10" cy="10" r="10" fill="#7cbf2e"/><circle cx="10" cy="10" r="5" fill="none" stroke="#fff" stroke-width="1.2"/><path d="M5 10h10M10 5c-2 2.8-2 7.2 0 10M10 5c2 2.8 2 7.2 0 10" fill="none" stroke="#fff" stroke-width="1.1"/></svg>
      www.yourwebsite.com
    </li>
  </ul>
  <div class="address-band">Your Address, City, State, Zip 0000, Country</div>
</section>

</body>
</html>
```